Sleek, Professional Business Card Design Needed

Business Cards - Logo Attached.

We are a solar consulting company. We are national and want our cards to represent the professional high quality products that we offer.

Industry/Entity Type

Business

Contact Information for Business Card

n/a

Requirements
Must have
• Design
• Name
• Position
• Number
• Email
• Address
Should not have
• Not be too crowded

```html
<!DOCTYPE html>
<html lang="en">
<head>
<meta charset="UTF-8">
<title>Sunridge Advisory – Business Card</title>
<link rel="stylesheet" href="https://fonts.googleapis.com/css2?family=Roboto:wght@400;500;700&display=swap">
<style>
  :root {
    --bg: #e3e3e3;
    --green: #66b23a;
    --teal: #12a0a0;
    --blue: #0a9fdc;
    --deep-blue: #1479b8;
    --brand-blue: #1b8fd2;
    --arc: #3a3d40;
    --paper: #f4f4f3;
    --white: #ffffff;
  }
  * { box-sizing: border-box; margin: 0; padding: 0; }
  html, body {
    width: 1200px; height: 576px; overflow: hidden;
    background: var(--bg);
    font-family: "Roboto", Arial, sans-serif;
  }
  .stage { position: relative; width: 1200px; height: 576px; }
  .card {
    position: absolute; top: 138px;
    width: 484px; height: 294px;
    border-radius: 14px; overflow: hidden;
  }
  /* Front */
  .card-front {
    left: 82px;
    background: linear-gradient(180deg, var(--green) 0%, #3fa65a 35%, var(--teal) 60%, var(--deep-blue) 100%);
    display: flex; flex-direction: column; align-items: center; justify-content: center;
    gap: 16px;
  }
  .front-mark {
    width: 74px; height: 74px; border-radius: 50%;
    border: 7px solid var(--white);
  }
  .front-name {
    color: var(--white); font-weight: 500; font-size: 30px; letter-spacing: 0.5px;
  }
  /* Back */
  .card-back { left: 602px; width: 482px; background: var(--paper); }
  .card-back svg.panel { position: absolute; inset: 0; }
  .contact-block { position: absolute; left: 23px; top: 0; color: var(--white); }
  .person-name { position: absolute; top: 24px; font-size: 22px; font-weight: 700; white-space: nowrap; }
  .person-role { position: absolute; top: 58px; font-size: 12px; white-space: nowrap; }
  .contact-list { position: absolute; top: 176px; list-style: none; font-size: 12.5px; }
  .contact-list li { display: flex; align-items: center; gap: 9px; height: 18px; white-space: nowrap; }
  .contact-list svg { width: 12px; height: 12px; fill: var(--white); flex: none; }
  .address { position: absolute; top: 232px; font-size: 12.5px; line-height: 17px; white-space: nowrap; }
  .back-brand {
    position: absolute; left: 268px; top: 70px; width: 190px;
    display: flex; flex-direction: column; align-items: center; gap: 14px;
  }
  .back-mark { width: 64px; height: 64px; border-radius: 50%; border: 6px solid var(--brand-blue); }
  .back-name { color: var(--brand-blue); font-weight: 500; font-size: 20px; white-space: nowrap; }
</style>
</head>
<body>
<main class="stage">
  <section class="card card-front" aria-label="Card front">
    <div class="front-mark"></div>
    <div class="front-name">SUNRIDGE ADVISORY</div>
  </section>

  <section class="card card-back" aria-label="Card back">
    <svg class="panel" viewBox="0 0 482 294" preserveAspectRatio="none" aria-hidden="true">
      <defs>
        <linearGradient id="panelFill" x1="0" y1="0" x2="0" y2="1">
          <stop offset="0" stop-color="#0a9fdc"/>
          <stop offset="0.4" stop-color="#16a6b4"/>
          <stop offset="0.65" stop-color="#4cae6a"/>
          <stop offset="1" stop-color="#6cb33e"/>
        </linearGradient>
      </defs>
      <path d="M0 0 H266 C230 60 214 130 222 180 C228 225 248 262 266 294 H0 Z" fill="url(#panelFill)"/>
      <path d="M276 0 H290 C252 50 232 110 230 175 C224 120 240 55 276 0 Z" fill="var(--arc)"/>
    </svg>

    <div class="contact-block">
      <h1 class="person-name">Daniel Reyes</h1>
      <p class="person-role">Managing Director</p>
      <ul class="contact-list">
        <li><svg viewBox="0 0 24 24"><path d="M6.6 10.8a15.1 15.1 0 0 0 6.6 6.6l2.2-2.2a1 1 0 0 1 1-.25 11.4 11.4 0 0 0 3.6.57 1 1 0 0 1 1 1V20a1 1 0 0 1-1 1A17 17 0 0 1 3 4a1 1 0 0 1 1-1h3.5a1 1 0 0 1 1 1c0 1.25.2 2.45.57 3.57a1 1 0 0 1-.25 1z"/></svg>1800-555-0147</li>
        <li><svg viewBox="0 0 24 24"><path d="M2 5h20v14H2z M2 5l10 8 10-8" stroke="#fff" stroke-width="0" /><path d="M3 6l9 7 9-7v12H3z" /></svg>dreyes@sunridge.com</li>
        <li><svg viewBox="0 0 24 24"><circle cx="12" cy="12" r="10"/></svg>www.sunridgeadvisory.com</li>
      </ul>
      <p class="address">48, Harbor Light Avenue<br>No, Country 456</p>
    </div>

    <div class="back-brand">
      <div class="back-mark"></div>
      <div class="back-name">SUNRIDGE ADVISORY</div>
    </div>
  </section>
</main>
</body>
</html>
```